Vantel company profile brochure

We are looking for a 2 - 4 page brochure for our company profile.
We’re Vantel, a team of town planning and traffic and transport engineering specialists located in Melbourne, Australia.
We would like a dynamic, exciting brochure that features the colours of our logo - blue, green and grey with orange as a feature colour.
The final result should convey that Vantel is:
-Reassuring and trustworthy
-Honest and direct
- Friendly and a bit kooky
-Laid-back and casual
-Fun to work with
-Highly knowledgeable within specific areas of expertise
-Polished and professional but not afraid to show a bit of personality
-Not as ‘hard edge’ as other planners or engineers
Vantel Consultants have created a business based on providing niche, expert advice across the two main areas of urban planning and traffic engineering as well as growing areas such as social and economic analysis. They are fiercely proud of the things that make them different to other firms – they take their responsibilities seriously, they are honest and up-front, they know how to work hard but also how to relax and have a laugh, and perhaps most importantly they know how to relate to people and they care about building successful relationships with their clients, colleagues and their staff. Vantel Consultants are united by our passion for shaping the city and their desire to ensure it develops sustainably.
Many similar businesses share some of these qualities, but Vantel is rare in that they deliver the whole package. This is evidenced by our ability to attract and retain high quality staff, by our long-standing client relationships and by their commitment to progressing our own company by commissioning a brochure and business card.

Target Market(s)

Vantel’s diverse client base consists of architecture practices, builders and developers, local government and the legal fraternity so these are the areas we market to.

Industry/Entity Type

Building

Requirements
Must have
• Must use our logos colours and logo.
The logo can be altered in that the type and image do not have stay exactly as it is on the JPEG - the words and image can be placed apart / together etc.
Nice to have
• We would like an image on the front cover that we can change
Page about disciplines

```html
<!DOCTYPE html>
<html lang="en">
<head>
<meta charset="utf-8">
<title>Vantel – Disciplines</title>
<link href="https://fonts.googleapis.com/css2?family=Arimo:wght@400;700&display=swap" rel="stylesheet">
<style>
  :root {
    --backdrop: #d6d6d6;
    --paper: #ffffff;
    --ink: #2b2b2b;
    --heading: #1f2a33;
    --leaf-light: #cfe79a;
    --leaf-mid: #7fbf3a;
    --leaf-dark: #3f8a1c;
    --sky: #8fb4d8;
    --sky-deep: #3f6fa8;
    --road: #5b5b5b;
    --grass: #6fa83a;
    --vest: #f07a1a;
    --car-grey: #b9bcc0;
  }
  * { box-sizing: border-box; margin: 0; padding: 0; }
  html, body { width: 1200px; height: 800px; overflow: hidden; }
  body {
    background: var(--backdrop);
    font-family: "Arimo", Arial, sans-serif;
    color: var(--ink);
    position: relative;
  }
  .page {
    position: absolute;
    top: 128px;
    width: 364px;
    height: 526px;
    background: var(--paper);
    overflow: hidden;
  }
  .page--left { left: 240px; }
  .page--right { left: 604px; }

  .photo { position: absolute; }
  .photo--leaves {
    left: 0; top: 44px; width: 364px; height: 134px;
    background: linear-gradient(180deg, var(--leaf-mid) 0%, var(--leaf-light) 55%, #e9f3cf 100%);
  }
  .photo--roads {
    left: 195px; top: 330px; width: 169px; height: 196px;
    background: linear-gradient(180deg, #c9d8e6 0%, #9ea6ad 45%, #6f7275 100%);
  }
  .photo--horizon {
    left: 26px; top: 6px; width: 138px; height: 134px;
    background: linear-gradient(180deg, var(--sky-deep) 0%, #c9dbee 55%, var(--road) 72%, var(--grass) 100%);
  }
  .photo--cars {
    left: 26px; top: 192px; width: 138px; height: 56px;
    background: linear-gradient(180deg, #f2f2f2 0%, var(--car-grey) 60%, #f2f2f2 100%);
  }
  .photo--worker {
    left: 0; top: 302px; width: 364px; height: 224px;
    background: linear-gradient(100deg, var(--vest) 0%, #c45f16 30%, #6d8fbf 55%, var(--sky) 75%, var(--grass) 100%);
  }

  .section-title {
    position: absolute;
    left: 46px; top: 156px;
    font-size: 14px;
    font-weight: 700;
    letter-spacing: 0.2px;
    color: var(--heading);
  }

  .column { position: absolute; font-size: 5.4px; line-height: 1.32; }
  .column--left-a { left: 46px; top: 180px; width: 136px; }
  .column--left-b { left: 195px; top: 186px; width: 160px; }
  .column--right-a { left: 26px; top: 146px; width: 138px; }
  .column--right-a.lower { top: 252px; }
  .column--right-b { left: 177px; top: 55px; width: 165px; }

  .discipline { margin-bottom: 7px; }
  .discipline h3 {
    font-size: 6px;
    font-weight: 700;
    color: var(--heading);
    margin-bottom: 1px;
  }
  .discipline h3.underlined { text-decoration: underline; }
</style>
</head>
<body>

<section class="page page--left">
  <div class="photo photo--leaves" role="img" aria-label="Fresh green leaves against a soft blurred green background"></div>
  <h2 class="section-title">DISCIPLINES</h2>

  <div class="column column--left-a">
    <div class="discipline">
      <h3>Planning</h3>
      <p>We use our extensive knowledge and experience to help our clients successfully navigate each step of the statutory and strategic planning processes.</p>
    </div>
    <div class="discipline">
      <h3>Permit Applications</h3>
      <p>We have obtained planning permits for our clients on a variety of residential, commercial, entertainment and industrial projects in Melbourne, regional Victoria and interstate. Our consultative approach and extensive experience allows us to identify and resolve potential issues quickly.</p>
    </div>
    <div class="discipline">
      <h3>VPAT Advocacy</h3>
      <p>Due to our industry expertise, Vantel’s planning team are regularly appointed as VPAT advocates for private and public clients. We have acted as representatives for diverse project types at VPAT appeals, mediations, planning panels and Consumer Standards Office appeals.</p>
    </div>
    <div class="discipline">
      <h3>VPAT Expert Evidence</h3>
      <p>XXXX [hyperlink to bio’s] frequently present expert evidence before VPAT and planning panels for a range of urban planning projects. They work closely with members of the legal fraternity, private and public clients to facilitate positive outcomes by applying their specialist knowledge.</p>
    </div>
    <div class="discipline">
      <h3>Traffic</h3>
      <p>Vantel’s traffic engineering experts assess, analyse and design road systems and traffic management plans, working closely with our planning and transport teams.</p>
    </div>
    <div class="discipline">
      <h3>Traffic Impact Assessment</h3>
      <p>Our team’s knowledge and experience gives us the ability to efficiently and accurately develop Traffic Impact Reports to accompany planning applications. We work across residential, commercial, industrial, sports and institutional projects and have worked with private developers and local government.</p>
    </div>
  </div>

  <div class="column column--left-b">
    <div class="discipline">
      <h3>VPAT Expert Evidence</h3>
      <p>XXXX [hyperlink to bio’s] frequently present expert evidence before VPAT and planning panels for a range of traffic projects. They assist members of the legal fraternity, private and public clients to facilitate positive outcomes by applying their specialist knowledge.</p>
    </div>
    <div class="discipline">
      <h3>Traffic System Design</h3>
      <p>We design and plan traffic facilities for private developers and government including the detailed design of traffic signal systems for urban arterial intersections. Our experience covers both the development of new systems and the design of upgrades to existing traffic system facilities.</p>
    </div>
    <div class="discipline">
      <h3>Local Area Traffic Management</h3>
      <p>Vantel collaborates with local governments to develop traffic management plans that address traffic safety and amenity issues for residential areas. We have worked on projects that feature highly sensitive, complex land uses such as schools, childcare centres and kindergartens.</p>
    </div>
  </div>

  <div class="photo photo--roads" role="img" aria-label="A pencil erasing a clear path through a tangle of roads, with a person walking along it"></div>
</section>

<section class="page page--right">
  <div class="photo photo--horizon" role="img" aria-label="An empty road running to the horizon under a blue sky with a red exclamation mark"></div>

  <div class="column column--right-a">
    <div class="discipline">
      <h3>Road Safety Audits</h3>
      <p>We plan and assess road safety for a range of private and public sector clients. Our extensive experience includes Municipal Road Safety Strategies for over 20 Victorian local councils as well as road safety audits for road works and proposed development sites.</p>
    </div>
  </div>

  <div class="photo photo--cars" role="img" aria-label="Rows of parked silver cars with one dark car in front"></div>

  <div class="column column--right-a lower">
    <div class="discipline">
      <h3>Car Parking</h3>
      <p>Vantel works with private and public clients, as well as architects and civil engineers, to prepare precinct parking plans, assess parking uses for new developments as well as assist with the planning and design of at-grade and multi-storey car parks.</p>
    </div>
  </div>

  <div class="column column--right-b">
    <div class="discipline">
      <h3 class="underlined">Transport</h3>
      <p>Vantel’s transport planning team offers our clients high level, accurate, strategic advice, which prioritises sustainable transport including walking, cycling and public transport.</p>
    </div>
    <div class="discipline">
      <h3>Sustainable Transport Planning</h3>
      <p>From public transport to bike-sharing, Vantel works with private and public clients to research, plan and recommend the most suitable sustainable transport solutions for the specific needs of each project. Where needed, our team seamlessly integrates with Vantel’s planning and traffic engineering teams.</p>
    </div>
    <div class="discipline">
      <h3>Green Travel Plans</h3>
      <p>Green travel is an increasing priority in today’s world – we work with multiple stakeholders to determine the best methods to promote and achieve sustainable transport options such as walking, cycling, car-sharing and public transport for a range of organisations including schools, workplaces and new development sites.</p>
    </div>
    <div class="discipline">
      <h3>Major Event Planning</h3>
      <p>Vantel works with major sports and entertainment event organisers to create safe and secure traffic plans that protect competitors, participants and spectators. We recognise the unique transport requirements of large-scale events and the difference that good planning makes.</p>
    </div>
    <div class="discipline">
      <h3>Bike Planning</h3>
      <p>Melbourne is known as a “cycle city” and Vantel’s transport team designs and assesses bicycle and pedestrian facilities, often as a component of larger road safety projects. We have experience with DDA compliance and our projects consider the special needs of pedestrians.</p>
    </div>
  </div>

  <div class="photo photo--worker" role="img" aria-label="A road worker in an orange safety vest crouching beside a traffic cone next to a green field under blue sky"></div>
</section>

</body>
</html>
```